Quartz and Granite Sealer Label

We need 2 labels for a sealer (Front/Back) that will protect elements from damaging quartz and granite for countertops floors and more.
For the FRONT LABEL We would like to see something to the effect of wine beading off a quartz/marble surface.

We like the words Shield, Guard, Protection, Quartz and Natural Stone Protection

The BACK label must have the following information
Product Benefits
-Latest technology in solvent-based fluoropolymer technology
-High Performing sealer that dries clear
-Odorless and FDA compliant solvent
-Breathable
-For interior and exterior use

Directions
Always test in inconspicuous area. Allow for a full 24 hour cure time to determine the desired result. Allow new grout installations to cure as directed (at least 24 hours.). Make sure surface is clean, dry and clear of waxes and coatings.

-Mask off any areas not intended to be treated
-Remove dirt and debris
-Allow sealer to penetrate stone for 15-30 minutes. Spread any excess over the surface to ensure proper penetration. Wipe off any remaining sealer before drying the surface. Apply a second or third coat for more porous surfaces. The second coat of sealer can be applied after 30 minutes. Wipe entire surface down with towel moistened with sealer to remove reside if needed.
-Wait at least 24-72 hours for sealer to cure.
-Foot traffic may begin after 5-7 hours.

Coverage & Wear
Coverage - 200-1500 sq ft per gallon
Expected Wear - Interior 3-5 years, Exterior 1-3 years

Caution: Combustible. Keep container closed and store in a cool environment. May cause eye and skin irritation. Use in a well ventilated area. Do not aerosolize.

Customer Service 1-800-555-0142

LABEL SIZES

Quart: 4.25” x 3.75” .125” bleed
Gallon: 5” x 6” .125” bleed

RGB Coloring

Target Market(s)

Homeowners

Industry/Entity Type

Kitchen and bath

Font styles to use
Sans Serif

Requirements
Must have
• Keywords - Premium Stain Protection, Impregnating Breathable Sealer,"Excellent on Quartz, Granite and Quartzite", Dries Clear, Simple Application,

```html
<!DOCTYPE html>
<html lang="en">
<head>
<meta charset="utf-8">
<title>Premium Stain Protection – Front and Back Labels</title>
<link rel="stylesheet" href="https://fonts.googleapis.com/css2?family=Montserrat:wght@400;500;600;700;800&family=Russo+One&display=swap">
<style>
:root{
  --canvas:#d9d9da;
  --blue-deep:#2f4fc6;
  --blue-mid:#3a6ad8;
  --blue-light:#3f8be6;
  --gold-dark:#8a5a1c;
  --gold:#c8923e;
  --gold-light:#e8b664;
  --green:#2a9a2a;
  --orange:#f36c0c;
  --white:#ffffff;
  --ink:#111111;
  --stone-light:#e2e2e0;
  --stone-mid:#bdbdbb;
}
*{box-sizing:border-box;margin:0;padding:0}
html,body{width:1200px;height:1200px;overflow:hidden}
body{background:var(--canvas);font-family:"Montserrat",sans-serif;position:relative}

.label{position:absolute;width:560px;height:494px;overflow:hidden;background:var(--white);box-shadow:0 6px 18px rgba(0,0,0,.18)}
.label--front{left:20px;top:353px}
.label--back{left:620px;top:353px}

/* ---------- front ---------- */
.front-stone{position:absolute;left:0;top:0;width:560px;height:250px;
  background:radial-gradient(circle at 60% 40%,var(--stone-light),var(--stone-mid))}
.front-corner{position:absolute;left:0;top:0;width:200px;height:142px}
.brand{position:absolute;left:14px;top:46px;display:flex;align-items:center;gap:8px}
.brand-dot{width:26px;height:26px;border-radius:50%;background:var(--blue-deep)}
.brand-name{font-family:"Montserrat",sans-serif;font-weight:800;font-size:22px;color:var(--blue-deep)}
.front-title{position:absolute;left:20px;top:152px;font-family:"Russo One",sans-serif;color:var(--ink);line-height:1}
.front-title .small{display:block;font-size:28px;letter-spacing:.5px}
.front-title .big{display:block;font-size:43px;margin-top:6px;letter-spacing:.5px}
.front-band{position:absolute;left:0;top:250px;width:344px;height:36px;
  background:linear-gradient(90deg,var(--gold-dark),var(--gold-light) 50%,var(--gold));
  color:var(--white);font-weight:700;font-size:20px;line-height:36px;padding-left:20px;letter-spacing:.3px}
.front-body{position:absolute;left:0;top:286px;width:560px;height:168px;
  background:linear-gradient(180deg,var(--blue-light),var(--blue-deep))}
.front-benefits{position:absolute;left:20px;top:296px;list-style:none;color:var(--white);font-size:15.5px;font-weight:500;line-height:24px}
.front-benefits li{padding-left:12px;text-indent:-12px}
.front-benefits li::before{content:"• "}
.front-shield{position:absolute;left:352px;top:32px;width:208px;height:390px;
  border-radius:40px 0 0 120px;background:linear-gradient(160deg,#bfe6fb,#35a0e8 55%,#1f6fcc)}
.front-footer{position:absolute;left:0;top:454px;width:560px;height:40px;background:var(--green);
  display:flex;justify-content:space-between;align-items:center;padding:0 20px;color:var(--white);font-weight:700;font-size:11px}

/* ---------- back ---------- */
.back-head{position:absolute;left:0;top:0;width:560px;height:98px}
.back-photo{position:absolute;left:340px;top:0;width:220px;height:98px;
  background:linear-gradient(90deg,#6f7a5a,#a8a48a 55%,#e0d8c6)}
.back-gold{position:absolute;left:0;top:0;width:365px;height:98px;
  background:linear-gradient(90deg,var(--gold-dark),var(--gold-light) 45%,var(--gold-dark));
  clip-path:polygon(0 0,100% 0,86% 100%,0 100%)}
.back-title{position:absolute;left:19px;top:18px;font-family:"Russo One",sans-serif;color:var(--white);line-height:1;
  text-shadow:0 2px 0 rgba(0,0,0,.6)}
.back-title .small{display:block;font-size:26px}
.back-title .big{display:block;font-size:41px;margin-top:3px}
.back-body{position:absolute;left:0;top:98px;width:560px;height:329px;
  background:linear-gradient(135deg,var(--blue-mid),var(--blue-deep) 50%,var(--blue-light))}
.section-title{color:var(--white);font-weight:700;font-size:15px;letter-spacing:.2px}
.benefits{position:absolute;left:20px;top:122px;width:250px}
.benefit-list{list-style:none;margin-top:9px}
.benefit-list li{display:flex;gap:8px;color:var(--white);font-size:12.5px;line-height:17px;margin-bottom:11px;font-weight:500}
.benefit-list svg{flex:none;width:17px;height:17px;margin-top:0}
.coverage{position:absolute;left:20px;top:339px;width:253px;height:57px;background:var(--green);padding:6px 12px;color:var(--white)}
.coverage h3{font-size:15px;font-weight:700;letter-spacing:.3px}
.coverage ul{margin-top:2px;padding-left:9px;font-size:7.6px;line-height:12px}
.directions{position:absolute;left:290px;top:121px;width:252px;color:var(--white)}
.directions p{margin-top:8px;font-size:8.2px;line-height:14.4px;text-align:justify}
.directions ul{margin-top:9px;padding-left:14px;font-size:8.2px;line-height:13.2px;text-align:justify}
.back-footer{position:absolute;left:0;top:427px;width:560px;height:67px;background:var(--white)}
.caution{position:absolute;left:20px;top:15px;width:200px;font-size:4.6px;line-height:6.4px;color:var(--ink)}
.caution strong{display:block;font-size:6px}
.hazard-icons{position:absolute;left:219px;top:12px;display:flex;gap:8px;align-items:center}
.service{position:absolute;left:372px;top:0;width:188px;height:67px;background:var(--orange);
  clip-path:polygon(10% 0,100% 0,100% 100%,0 100%);color:var(--white);padding:13px 0 0 30px}
.service .lbl{font-size:11px;font-weight:700}
.service .num{font-size:17px;font-weight:800;margin-top:2px}
</style>
</head>
<body>

<section class="label label--front" aria-label="Front label">
  <div class="front-stone" role="img" aria-label="Light grey quartz stone surface texture"></div>
  <svg class="front-corner" viewBox="0 0 200 142" aria-hidden="true">
    <path d="M0 0H200C185 40 178 100 140 128C125 138 100 140 0 140Z" fill="var(--gold)"/>
    <path d="M0 0H188C174 40 166 96 132 120C118 130 95 132 0 132Z" fill="var(--white)"/>
  </svg>
  <div class="brand"><span class="brand-dot"></span><span class="brand-name">Lumera</span></div>
  <div class="front-shield" role="img" aria-label="Glossy blue protective shield illustration"></div>
  <h1 class="front-title"><span class="small">PREMIUM STAIN</span><span class="big">PROTECTION</span></h1>
  <div class="front-body"></div>
  <div class="front-band">COUNTERTOP PROTECTOR</div>
  <ul class="front-benefits">
    <li>Strong protection repels spills</li>
    <li>Ideal for Quartz, Quartzite &amp; Granite</li>
    <li>Simple, two-step application</li>
    <li>Dries clear and odorless</li>
    <li>Doesn’t impede Quartz or natural<br>stone’s breathability</li>
  </ul>
  <div class="front-footer"><span>1 quart (946 ML)</span><span>Low VOC &lt;100 G/L</span><span>Read Back Panel for Cautions</span></div>
</section>

<section class="label label--back" aria-label="Back label">
  <div class="back-head">
    <div class="back-photo" role="img" aria-label="Stone surface before and after sealing"></div>
    <div class="back-gold"></div>
    <h2 class="back-title"><span class="small">PREMIUM STAIN</span><span class="big">PROTECTION</span></h2>
  </div>
  <div class="back-body"></div>

  <div class="benefits">
    <h3 class="section-title">PRODUCT BENEFITS</h3>
    <ul class="benefit-list">
      <li><svg viewBox="0 0 20 20"><circle cx="10" cy="10" r="9" fill="var(--white)"/><circle cx="10" cy="10" r="7" fill="var(--green)"/><path d="M6 10.3l2.7 2.7L14 7.6" stroke="var(--white)" stroke-width="2" fill="none"/></svg><span>Latest technology in solvent-based fluoropolymer technology</span></li>
      <li><svg viewBox="0 0 20 20"><circle cx="10" cy="10" r="9" fill="var(--white)"/><circle cx="10" cy="10" r="7" fill="var(--green)"/><path d="M6 10.3l2.7 2.7L14 7.6" stroke="var(--white)" stroke-width="2" fill="none"/></svg><span>High Performing sealer that dries clear</span></li>
      <li><svg viewBox="0 0 20 20"><circle cx="10" cy="10" r="9" fill="var(--white)"/><circle cx="10" cy="10" r="7" fill="var(--green)"/><path d="M6 10.3l2.7 2.7L14 7.6" stroke="var(--white)" stroke-width="2" fill="none"/></svg><span>Odorless and FDA compliant solvent</span></li>
      <li><svg viewBox="0 0 20 20"><circle cx="10" cy="10" r="9" fill="var(--white)"/><circle cx="10" cy="10" r="7" fill="var(--green)"/><path d="M6 10.3l2.7 2.7L14 7.6" stroke="var(--white)" stroke-width="2" fill="none"/></svg><span>Breathable</span></li>
      <li><svg viewBox="0 0 20 20"><circle cx="10" cy="10" r="9" fill="var(--white)"/><circle cx="10" cy="10" r="7" fill="var(--green)"/><path d="M6 10.3l2.7 2.7L14 7.6" stroke="var(--white)" stroke-width="2" fill="none"/></svg><span>For interior and exterior use</span></li>
    </ul>
  </div>

  <div class="coverage">
    <h3>COVERAGE &amp; WEAR</h3>
    <ul>
      <li>Coverage - 200-1500 sq ft per gallon</li>
      <li>Expected Wear - Interior 3-5 years, Exterior 1-3 years</li>
    </ul>
  </div>

  <div class="directions">
    <h3 class="section-title">DIRECTIONS</h3>
    <p>Always test in inconspicuous area. Allow for a full 24 hour cure time to determine the desired result. Allow new grout installations to cure as directed (at least 24 hours.). Make sure surface is clean, dry and clear of waxes and coatings.</p>
    <ul>
      <li>Mask off any areas not intended to be treated</li>
      <li>Remove dirt and debris</li>
      <li>Allow sealer to penetrate stone for 15-30 minutes. Spread any excess over the surface to ensure proper penetration. Wipe off any remaining sealer before drying the surface. Apply a second or third coat for more porous surfaces. The second coat of sealer can be applied after 30 minutes. Wipe entire surface down with towel moistened with sealer to remove reside if needed.</li>
      <li>Wait at least 24-72 hours for sealer to cure.</li>
      <li>Foot traffic may begin after 5-7 hours.</li>
    </ul>
  </div>

  <div class="back-footer">
    <div class="caution"><strong>CAUTION:</strong>Combustible. Keep container closed and store in a cool environment. May cause eye and skin irritation. Use in a well ventilated area. Do not aerosolize.</div>
    <div class="hazard-icons">
      <svg width="40" height="40" viewBox="0 0 40 40" aria-label="Flammable hazard"><rect x="8" y="8" width="24" height="24" transform="rotate(45 20 20)" fill="var(--white)" stroke="#d01818" stroke-width="2.5"/><path d="M20 12c4 5 5 8 3 12 2-1 3-3 3-5 2 4 0 9-6 9s-8-5-5-10c0 2 1 3 2 3-1-3 0-6 3-9Z" fill="var(--ink)"/><rect x="13" y="27" width="14" height="2" fill="var(--ink)"/></svg>
      <svg width="34" height="34" viewBox="0 0 34 34" aria-label="Wear respirator"><circle cx="17" cy="17" r="16" fill="var(--green)"/><circle cx="17" cy="17" r="10" fill="none" stroke="var(--white)" stroke-width="2.5"/></svg>
      <svg width="34" height="34" viewBox="0 0 34 34" aria-label="Wear gloves"><circle cx="17" cy="17" r="16" fill="var(--green)"/><rect x="11" y="9" width="12" height="16" rx="4" fill="var(--white)"/></svg>
      <svg width="34" height="34" viewBox="0 0 34 34" aria-label="Wear eye protection"><circle cx="17" cy="17" r="16" fill="var(--green)"/><rect x="8" y="14" width="18" height="6" rx="3" fill="var(--white)"/></svg>
    </div>
    <div class="service"><div class="lbl">Customer Service</div><div class="num">1-800-555-0142</div></div>
  </div>
</section>

</body>
</html>
```